International Digitally Led Media Agency Requires a New Website

Brief Outline

• We are a growing business that has been established for approximately 2 years.

• Our current website did the job when Corvend Media began but it has not developed and progressed alongside the business (currently it does not represent nor portray the business appropriately).

• Corvend Media is a digitally led media agency that has numerous arms; 1) production based work (e.g. Paid Advertising, etc.) 2) consultancy and 3) Offline media (such as outdoor, TV, Radio)

• The business is globally focused and the website must reflect this.

• The new website is to portray the business more professionally with thought leadership at the forefront.

• The tone and voice of the website is to be clear, concise and straight talking.

• The website isn't to be a driver of new business (e.g. conversion based for enquiries) but is to support external new business activities. However, the website is to support the thought leadership marketing (specifically around content marketing - webinars, whitepapers, social, etc).

• We must be able to edit/upload/add content to the website very easily.

The current website is www.corvend-media.example

Current clients include
J&T - www.j&t.example
Folmary Trudesse - www.ft.example
KX Glow - www.kxglow.example
Lungwise UK - www.lungwise.example.uk
The Vantry Academy - www.vantry-academy.example.uk
Hale Retirement - www.haleretirement.example
Quillet Credit - www.quilletcredit.example.uk
DLMorvat - www.dl-morvat.example.uk
Perravine Lodging Collective - www.plc-lodging.example
Brindlewick - www.brindlewick.example
Varnique - www.varniqueit.example

Reason: We gave some delayed feedback to some desginers looking to enter the project and want to give them a chance to submit their designs.

Target Market(s)

Key decision makers within brands. Marketing Executives/Managers/Directors, Procurement Executives/Managers/Directors, Company Owners, CEO's /MD's

Industry/Entity Type

Business

Coding

Coded - Design and coding required

Number of Pages Required

5+ page

Font styles to use
Sans Serif

Requirements
Must have
• We definitely want video capability and the ability to add pages ourselves.
• We would like the layout to look something like
• HOME
•   
• 7dash3 > CASE STUDIES
• WHAT WE DO > CASE STUDIES
•  
• CONTACT
•  
• CLIENT LOGIN
Nice to have
• Social feeds

```html
<!DOCTYPE html>
<html lang="en">
<head>
<meta charset="utf-8">
<title>Corvend Media</title>
<link href="https://fonts.googleapis.com/css2?family=Ubuntu:wght@300;400;500;700&display=swap" rel="stylesheet">
<style>
:root{
  --gold:#c99a3c;
  --gold-deep:#b4852a;
  --gold-soft:#e3c78e;
  --ink:#262626;
  --text:#4a4a4a;
  --muted:#777;
  --panel:#f1f1f1;
  --frame:#e4e4e4;
  --white:#ffffff;
  --slate:#5a5a5a;
}
*{box-sizing:border-box;margin:0;padding:0}
html,body{width:1200px;height:3557px;overflow:hidden}
body{background:var(--frame);font-family:'Ubuntu',Arial,sans-serif;color:var(--ink)}
.page{position:absolute;left:18px;top:0;width:1164px;height:3545px;background:var(--white);overflow:hidden}
section,header,footer{position:absolute;left:0;width:1164px}
.abs{position:absolute}

/* header */
.site-header{top:0;height:138px;background:var(--white);z-index:3}
.contact-tab{left:609px;top:12px;width:533px;height:35px;background:var(--gold);
  clip-path:polygon(18px 0,100% 0,100% 100%,0 100%);display:flex;align-items:center;gap:14px;padding-left:40px;color:var(--white);font-size:12px;font-weight:500}
.contact-tab span{display:flex;align-items:center;gap:6px}
.social-dots{display:flex;gap:5px;margin-left:4px}
.social-dots i{width:17px;height:17px;border:1.5px solid var(--white);border-radius:50%;display:block}
.brand{left:42px;top:36px;display:flex;align-items:center;gap:14px}
.brand-disc{width:130px;height:130px;border-radius:50%;background:var(--white);box-shadow:0 3px 8px rgba(0,0,0,.18)}
.brand-name{margin-top:-16px;font-size:22px;font-weight:500;color:var(--ink);white-space:nowrap}
.main-nav{right:42px;top:94px;display:flex;gap:40px;font-size:13.5px;font-weight:700;color:var(--ink)}
.main-nav a{color:inherit;text-decoration:none;position:relative}
.main-nav a.current{color:var(--gold)}
.main-nav a.current::before{content:"";position:absolute;left:50%;top:50%;width:64px;height:64px;margin:-33px 0 0 -32px;border-radius:50%;border:2px solid var(--gold);border-right-color:transparent}

/* hero */
.hero{top:138px;height:554px;background:
  radial-gradient(ellipse 260px 320px at 230px 300px,#2b3340 0%,rgba(43,51,64,0) 100%),
  radial-gradient(ellipse 380px 260px at 760px 180px,#bfe6f7 0%,rgba(191,230,247,0) 100%),
  linear-gradient(100deg,#1f4560 0%,#2c79a8 45%,#4da8d6 75%,#2d86b8 100%)}

/* intro band */
.intro-band{top:692px;height:190px;background:linear-gradient(180deg,#f4f4f4 0%,#d9d9d9 100%);box-shadow:0 6px 10px rgba(0,0,0,.15);z-index:2}
.intro-title{left:47px;top:42px;font-size:50px;line-height:52px;font-weight:700;letter-spacing:-.5px}
.intro-title .gold{color:var(--gold)}
.intro-title .dark{color:#333}
.intro-rule{left:340px;top:42px;width:2px;height:106px;background:#bbb}
.intro-copy{left:372px;top:50px;width:740px;font-size:17px;line-height:25px;font-weight:700;color:#3a3a3a}

/* shared section heading */
.sec-head{left:0;width:1164px;display:flex;align-items:center;justify-content:center;gap:12px;font-size:21px;font-weight:700;color:var(--ink);text-transform:uppercase;white-space:nowrap}
.sec-head .gold{color:var(--gold)}
.head-mark{width:40px;height:40px;border-radius:50%;border:2px solid var(--gold);background:var(--white);flex:none}
.sec-head.lined::before,.sec-head.lined::after{content:"";width:250px;height:1px;background:#cfcfcf;margin:0 14px;flex:none}

/* clarity */
.clarity{top:882px;height:593px;background:var(--white)}
.clarity .sec-head{top:60px}
.pillars{left:60px;top:122px;width:1044px;display:grid;grid-template-columns:repeat(4,1fr)}
.pillar{text-align:center;font-size:12.5px;line-height:17px;font-weight:700;color:#333;padding:0 40px}
.pillar-icon{width:118px;height:118px;margin:0 auto 14px;border-radius:50%;background:var(--white);box-shadow:0 2px 6px rgba(0,0,0,.15);position:relative;display:flex;align-items:center;justify-content:center}
.pillar-icon::before{content:"";position:absolute;inset:-6px;border-radius:50%;border:4px solid var(--gold);border-bottom-color:transparent;border-right-color:transparent;transform:rotate(-20deg)}
.tagline{left:0;width:1164px;top:398px;text-align:center;font-size:18px;font-weight:700;color:var(--ink)}
.actions{left:260px;top:478px;display:flex;gap:36px}
.pill-btn{position:relative;width:290px;height:40px;border-radius:20px;background:var(--gold);color:var(--white);font-size:14px;font-weight:700;display:flex;align-items:center;justify-content:center;padding-left:40px;box-shadow:0 3px 4px rgba(0,0,0,.2)}
.pill-btn::before{content:"";position:absolute;left:-10px;top:-10px;width:60px;height:60px;border-radius:50%;background:var(--white);box-shadow:0 2px 6px rgba(0,0,0,.2)}

/* 7dash3 */
.method{top:1475px;height:505px;background:var(--panel)}
.method .sec-head{top:58px}
.method-board{left:88px;top:156px;width:1019px;height:220px;border:2px solid var(--gold);border-radius:8px;background:var(--white);display:grid;grid-template-columns:1fr 1fr 1fr}
.step{position:relative;padding:68px 22px 0 36px;font-size:12.5px;line-height:17px;color:#444}
.step.featured{background:var(--gold);color:var(--white);margin-top:-26px;padding-top:94px}
.step h3{position:absolute;left:112px;top:14px;font-size:15px;font-weight:700;color:var(--ink)}
.step.featured h3{top:42px;left:84px;color:var(--white)}
.step-icon{position:absolute;left:18px;top:-30px;width:84px;height:84px;border-radius:50%;background:var(--white);border:3px solid var(--gold);display:flex;align-items:center;justify-content:center;box-shadow:0 2px 5px rgba(0,0,0,.15)}
.step.featured .step-icon{left:-10px;top:-8px}
.dark-btn{left:482px;top:422px;width:200px;height:36px;border-radius:6px;background:var(--slate);color:var(--white);font-size:13px;font-weight:700;display:flex;align-items:center;justify-content:center}

/* what we do */
.services{top:1980px;height:605px;background:linear-gradient(180deg,#d5d5d5 0%,#e8e8e8 40%,#cfcfcf 100%)}
.services .sec-head{top:58px}
.svc-label{font-size:12.5px;line-height:16px;font-weight:700;color:#333}
.svc-label h4{font-size:13px;color:var(--gold);text-transform:uppercase;margin-bottom:3px}
.svc-cols{display:flex;gap:40px}
.strategy-box{left:92px;top:297px;width:297px;height:137px;background:rgba(201,154,60,.85)}
.strategy-box .svc-label{position:absolute;left:18px;top:20px;color:var(--white)}
.strategy-box .svc-label h4{color:var(--white)}
.node{width:96px;height:96px;border-radius:50%;background:var(--white);border:3px solid var(--gold-soft);box-shadow:0 2px 6px rgba(0,0,0,.2);display:flex;align-items:center;justify-content:center}

/* clients */
.clients{top:2585px;height:256px;background:var(--white)}
.clients .sec-head{top:58px}
.client-row{left:100px;top:132px;width:964px;display:flex;justify-content:space-between;align-items:center}
.client{display:flex;align-items:center;gap:8px;font-size:17px;font-weight:700;color:var(--slate);line-height:19px}
.client i{width:14px;height:14px;background:var(--slate);display:block;flex:none}
.client i.round{border-radius:50%}
.arrow{top:152px;width:26px;height:30px}

/* feeds */
.feeds{top:2841px;height:379px;background:var(--panel)}
.feeds .sec-head{top:58px}
.feed-row{left:40px;top:134px;width:1100px;display:grid;grid-template-columns:repeat(3,1fr);gap:24px}
.feed{display:flex;gap:16px}
.feed-date{width:62px;flex:none;text-align:center;background:var(--white);box-shadow:0 1px 3px rgba(0,0,0,.12)}
.feed-date b{display:block;font-size:30px;line-height:32px;color:var(--gold);padding-top:4px}
.feed-date small{display:block;font-size:11px;font-weight:700;color:var(--gold);padding-bottom:3px}
.feed-date em{display:block;font-style:normal;background:var(--gold);color:var(--white);font-size:12px;font-weight:700;padding:3px 0}
.feed p{font-size:12px;line-height:15px;color:#555}
.feed p strong{color:#333}
.follow{left:490px;top:270px;width:184px;height:26px;border-radius:4px;background:#e6e6e6;border:1px solid #c9c9c9;display:flex;align-items:center;justify-content:center;gap:7px;font-size:11px;color:#444}
.follow i{width:11px;height:11px;border-radius:50%;background:#8aa9c0;display:block}

/* footer */
.site-footer{top:3220px;height:285px;background:var(--gold);color:var(--white)}
.foot-disc{left:48px;top:-2px;width:110px;height:110px;border-radius:50%;border:3px solid var(--white)}
.foot-name{left:40px;top:120px;width:126px;text-align:center;font-size:13px;font-weight:500}
.foot-col{top:46px}
.foot-col h5{font-size:12px;font-weight:700;text-transform:uppercase;padding-bottom:10px;border-bottom:1px solid rgba(255,255,255,.6);margin-bottom:9px}
.foot-col ul{list-style:none;font-size:11px;line-height:17px;font-weight:500;text-transform:uppercase}
.foot-col li::before{content:"› "}
.contact-line{display:flex;gap:9px;align-items:flex-start;font-size:11px;line-height:16px;font-weight:500;margin-bottom:14px}
.contact-line svg{flex:none}
.badge{width:78px;height:94px}
.copyright{top:3505px;height:40px;background:#f6f6f6;display:flex;align-items:center;justify-content:space-between;padding:0 24px;font-size:9px;color:#666}
.copyright .social-dots i{border-color:#888;width:14px;height:14px}
</style>
</head>
<body>
<div class="page">

  <header class="site-header">
    <div class="abs contact-tab">
      <span><svg width="12" height="12" viewBox="0 0 24 24"><path fill="#fff" d="M6.6 10.8a15 15 0 0 0 6.6 6.6l2.2-2.2c.3-.3.7-.4 1-.2 1.1.4 2.3.6 3.6.6.6 0 1 .4 1 1V20c0 .6-.4 1-1 1A17 17 0 0 1 3 4c0-.6.4-1 1-1h3.5c.6 0 1 .4 1 1 0 1.3.2 2.5.6 3.6.1.3 0 .7-.2 1z"/></svg>+44 20 7946 0321</span>
      <span><svg width="13" height="10" viewBox="0 0 26 20"><rect x="1" y="1" width="24" height="18" fill="none" stroke="#fff" stroke-width="2"/><path d="M1 1l12 10L25 1" fill="none" stroke="#fff" stroke-width="2"/></svg>contact@corvend-media.example</span>
      <span class="social-dots"><i></i><i></i><i></i></span>
    </div>
    <div class="abs brand">
      <div class="brand-disc"></div>
      <div class="brand-name">Corvend Media</div>
    </div>
    <nav class="abs main-nav">
      <a class="current" href="#">HOME</a>
      <a href="#">7DASH3</a>
      <a href="#">WHAT WE DO</a>
      <a href="#">CONTACT</a>
      <a href="#">CLIENT LOGIN</a>
    </nav>
  </header>

  <section class="hero" role="img" aria-label="Photo of a businessman in a suit touching a glowing holographic interface of digital icons"></section>

  <section class="intro-band">
    <h1 class="abs intro-title"><span class="gold">WE MAKE</span><br><span class="dark">AMAZING</span></h1>
    <div class="abs intro-rule"></div>
    <p class="abs intro-copy">Tapping away on our computers in a side street just off Halden Street in Central London is where you will find us - Corvend Media. We are a digitally led Media agency fuelled by the belief that every client deserves “Amazing” work.</p>
  </section>

  <section class="clarity">
    <h2 class="abs sec-head lined"><span class="head-mark"></span><span><span class="gold">We keep fighting to</span> give you clarity by:</span></h2>
    <div class="abs pillars">
      <div class="pillar">
        <div class="pillar-icon"><svg width="56" height="44" viewBox="0 0 56 44"><rect x="8" y="4" width="40" height="28" rx="2" fill="none" stroke="#333" stroke-width="3"/><path d="M2 38h52" stroke="#333" stroke-width="4"/><circle cx="26" cy="17" r="6" fill="none" stroke="#333" stroke-width="2.5"/><path d="M30 21l6 6" stroke="#333" stroke-width="3"/></svg></div>
        Creating a singular view of your digital ecosystem
      </div>
      <div class="pillar">
        <div class="pillar-icon"><svg width="54" height="54" viewBox="0 0 54 54"><circle cx="27" cy="10" r="7" fill="none" stroke="#333" stroke-width="2.5"/><rect x="3" y="32" width="14" height="12" fill="none" stroke="#333" stroke-width="2.5"/><rect x="37" y="32" width="14" height="12" fill="none" stroke="#333" stroke-width="2.5"/><path d="M27 17v8M10 32v-7h34v7" fill="none" stroke="#333" stroke-width="2.5"/></svg></div>
        Reviewing how and why your money is being spent where it is
      </div>
      <div class="pillar">
        <div class="pillar-icon"><svg width="56" height="48" viewBox="0 0 56 48"><g fill="#333"><circle cx="28" cy="6" r="4"/><circle cx="12" cy="20" r="4"/><circle cx="28" cy="20" r="4"/><circle cx="44" cy="20" r="4"/><rect x="6" y="26" width="12" height="18" rx="3"/><rect x="22" y="26" width="12" height="18" rx="3"/><rect x="38" y="26" width="12" height="18" rx="3"/></g></svg></div>
        Profiling your customers. We understand you may have 1000s of different customers with different motivations, interests and value to your brand
      </div>
      <div class="pillar">
        <div class="pillar-icon"><svg width="56" height="54" viewBox="0 0 56 54"><g stroke="#333" stroke-width="2" fill="none"><path d="M28 26L10 10M28 26L46 8M28 26L8 38M28 26L48 40M10 10L46 8M8 38L48 40"/></g><g fill="#333"><circle cx="28" cy="26" r="6"/><circle cx="10" cy="10" r="4"/><circle cx="46" cy="8" r="4"/><circle cx="8" cy="38" r="4"/><circle cx="48" cy="40" r="4"/><path d="M20 52c0-6 4-9 8-9s8 3 8 9z"/></g></svg></div>
        Finding the best digital channels to communicate with your customers
      </div>
    </div>
    <p class="abs tagline">Because everything is changing every day...exciting isn’t it! Never stop, never settle, always improve. Be amazing.</p>
    <div class="abs actions">
      <div class="pill-btn">REQUEST A DEMO</div>
      <div class="pill-btn">DISCOVER MORE</div>
    </div>
  </section>

  <section class="method">
    <h2 class="abs sec-head"><span class="head-mark"></span><span class="gold">7dash3</span></h2>
    <div class="abs method-board">
      <div class="step">
        <div class="step-icon"><svg width="44" height="44" viewBox="0 0 44 44"><g stroke="#c99a3c" stroke-width="2.5" fill="none"><circle cx="22" cy="22" r="7"/><path d="M22 15V5M22 29v10M15 22H5M29 22h10"/></g><g fill="#c99a3c"><circle cx="22" cy="5" r="3"/><circle cx="22" cy="39" r="3"/><circle cx="5" cy="22" r="3"/><circle cx="39" cy="22" r="3"/></g></svg></div>
        <h3>ANALYSE IT</h3>
        <p>Regardless of your current agency situation we will give you an independent view on your strengths and weaknesses in media strategy, resource and execution.</p>
      </div>
      <div class="step featured">
        <div class="step-icon"><svg width="44" height="44" viewBox="0 0 44 44"><g stroke="#333" stroke-width="2.5" fill="none"><rect x="14" y="3" width="16" height="12"/><path d="M22 15v8M9 23h26M9 23v6M35 23v6"/><circle cx="9" cy="34" r="5"/><rect x="30" y="29" width="10" height="10"/></g></svg></div>
        <h3>PLAN IT</h3>
        <p>Focusing on what matters to your business most, we find the right blend of granular, strategic and detailed approaches to help you achieve your goals.</p>
      </div>
      <div class="step">
        <div class="step-icon"><svg width="44" height="44" viewBox="0 0 44 44"><g stroke="#c99a3c" stroke-width="3" fill="none"><circle cx="20" cy="24" r="16"/><circle cx="20" cy="24" r="9"/></g><circle cx="20" cy="24" r="3" fill="#c99a3c"/><path d="M20 24L38 6M32 6h6v6" stroke="#c99a3c" stroke-width="3" fill="none"/></svg></div>
        <h3>SMASH IT</h3>
        <p>The old adage is true - Knowledge is power. Our clients make decisions with confidence because we give them clarity on their media ecosystem.</p>
      </div>
    </div>
    <div class="abs dark-btn">VIEW CASE STUDIES</div>
  </section>

  <section class="services">
    <div class="abs" style="inset:0" role="img" aria-label="Faded grey photo of a wall of digital screens"></div>
    <h2 class="abs sec-head"><span><span class="gold">What</span> we do</span></h2>

    <svg class="abs" style="left:0;top:0" width="1164" height="605" viewBox="0 0 1164 605">
      <path d="M396 600V505a190 190 0 0 1 380 0V600h-70V505a120 120 0 0 0-240 0V600z" fill="#c99a3c"/>
      <path d="M466 505a120 120 0 0 1 240 0" fill="none" stroke="#a87a22" stroke-width="4"/>
      <g stroke="#fff" stroke-width="2" fill="#fff">
        <line x1="581" y1="233" x2="581" y2="316"/><circle cx="581" cy="316" r="4"/>
        <line x1="368" y1="404" x2="420" y2="430"/><circle cx="420" cy="430" r="4"/>
        <line x1="798" y1="404" x2="748" y2="430"/><circle cx="748" cy="430" r="4"/>
      </g>
      <g font-family="Ubuntu, Arial, sans-serif" font-size="22" font-weight="700" fill="#fff">
        <text x="438" y="490">01</text><text x="566" y="392">02</text><text x="708" y="490">03</text>
      </g>
      <circle cx="586" cy="510" r="82" fill="#fff" stroke="#e0d2b3" stroke-width="4"/>
    </svg>

    <div class="abs svc-label" style="left:306px;top:136px">
      <h4>Planning &amp; Buying</h4>
      <div class="svc-cols">
        <div>Programmatic<br>TV<br>Press<br>Outdoor</div>
        <div>Paid Social<br>Paid Search<br>Mobile<br>Digital Impact</div>
      </div>
    </div>
    <div class="abs node" style="left:533px;top:137px"><svg width="44" height="44" viewBox="0 0 44 44"><g stroke="#c99a3c" stroke-width="2.5" fill="none"><rect x="6" y="6" width="32" height="24"/><path d="M14 22v-6M22 22V12M30 22v-8M14 38l8-8 8 8"/></g></svg></div>

    <div class="abs strategy-box">
      <div class="svc-label"><h4>Media Strategy</h4>Insight<br>Research<br>KPI Setting<br>Forecasting</div>
    </div>
    <div class="abs node" style="left:272px;top:308px"><svg width="44" height="44" viewBox="0 0 44 44"><g fill="#c99a3c"><rect x="6" y="6" width="14" height="14"/><rect x="24" y="6" width="14" height="14" opacity=".6"/><rect x="6" y="24" width="14" height="14" opacity=".6"/><rect x="24" y="24" width="14" height="14"/></g></svg></div>

    <div class="abs node" style="left:798px;top:308px"><svg width="44" height="40" viewBox="0 0 44 40"><path d="M4 32l11-12 9 8 16-20" fill="none" stroke="#c99a3c" stroke-width="3"/><g fill="#c99a3c"><circle cx="4" cy="32" r="3"/><circle cx="15" cy="20" r="3"/><circle cx="24" cy="28" r="3"/><circle cx="40" cy="8" r="3"/></g></svg></div>
    <div class="abs svc-label" style="left:922px;top:310px">
      <h4>Data &amp; Insights</h4>Web Analytics<br>Content optimisation<br>A/B Testing<br>Tag Management<br>Live Bespoke Dashboards
    </div>
  </section>

  <section class="clients">
    <h2 class="abs sec-head"><span class="head-mark"></span><span><span class="gold">Our</span> clients</span></h2>
    <svg class="abs arrow" style="left:48px" viewBox="0 0 26 30"><path d="M18 3L6 15l12 12" fill="none" stroke="#999" stroke-width="3"/></svg>
    <div class="abs client-row">
      <div class="client"><i class="round"></i>The Vantry Academy</div>
      <div class="client">Hale Retirement</div>
      <div class="client"><i class="round"></i>Quillet Credit</div>
      <div class="client">Perravine Lodging<br>Collective</div>
      <div class="client"><i></i>Brindlewick</div>
    </div>
    <svg class="abs arrow" style="left:1092px" viewBox="0 0 26 30"><path d="M8 3l12 12L8 27" fill="none" stroke="#999" stroke-width="3"/></svg>
  </section>

  <section class="feeds">
    <h2 class="abs sec-head"><span class="head-mark"></span><span><span class="gold">Latest</span> feeds</span></h2>
    <div class="abs feed-row">
      <article class="feed">
        <div class="feed-date"><b>01</b><small>SEP</small><em>2016</em></div>
        <p><strong>Nam liber tempor cum soluta nobis</strong><br>Lorem ipsum dolor sit amet, consectetuer adipiscing elit, sed diam nonummy nibh euismod tincidunt ut laoreet dolore magna aliquam erat.</p>
      </article>
      <article class="feed">
        <div class="feed-date"><b>24</b><small>AUG</small><em>2016</em></div>
        <p><strong>Nam liber tempor cum soluta nobis</strong><br>Lorem ipsum dolor sit amet, consectetuer adipiscing elit, sed diam nonummy nibh euismod tincidunt ut laoreet dolore magna aliquam erat.</p>
      </article>
      <article class="feed">
        <div class="feed-date"><b>24</b><small>AUG</small><em>2016</em></div>
        <p><strong>Nam liber tempor cum soluta nobis</strong><br>Lorem ipsum dolor sit amet, consectetuer adipiscing elit, sed diam nonummy nibh euismod tincidunt ut laoreet dolore magna aliquam erat.</p>
      </article>
    </div>
    <div class="abs follow"><i></i>Follow @CorvendMedia</div>
  </section>

  <footer class="site-footer">
    <div class="abs foot-disc"></div>
    <div class="abs foot-name">Corvend Media</div>
    <div class="abs foot-col" style="left:213px;width:120px">
      <h5>Quick Links</h5>
      <ul><li>Home</li><li>7dash3</li><li>What WeDo</li><li>Contact</li><li>Client Login</li></ul>
    </div>
    <div class="abs foot-col" style="left:367px;width:110px">
      <h5>7dash3</h5>
      <ul><li>Analyse It</li><li>Plan It</li><li>Smash It</li></ul>
    </div>
    <div class="abs foot-col" style="left:507px;width:160px">
      <h5>What We Do</h5>
      <ul><li>Media Strategy</li><li>Planning &amp; Buying</li><li>Data &amp; Insights</li></ul>
    </div>
    <div class="abs foot-col" style="left:704px;width:200px">
      <h5>Contact</h5>
      <div class="contact-line"><svg width="14" height="18" viewBox="0 0 14 18"><path d="M7 1a6 6 0 0 0-6 6c0 4.5 6 10 6 10s6-5.5 6-10a6 6 0 0 0-6-6z" fill="none" stroke="#fff" stroke-width="1.8"/><circle cx="7" cy="7" r="2" fill="#fff"/></svg><span>CORVEND MEDIA<br>14 MARLOW YARD<br>LONDON<br>W1X 9ZZ</span></div>
      <div class="contact-line"><svg width="14" height="14" viewBox="0 0 24 24"><path fill="#fff" d="M6.6 10.8a15 15 0 0 0 6.6 6.6l2.2-2.2c.3-.3.7-.4 1-.2 1.1.4 2.3.6 3.6.6.6 0 1 .4 1 1V20c0 .6-.4 1-1 1A17 17 0 0 1 3 4c0-.6.4-1 1-1h3.5c.6 0 1 .4 1 1 0 1.3.2 2.5.6 3.6.1.3 0 .7-.2 1z"/></svg><span>+44 20 7946 0321</span></div>
      <div class="contact-line"><svg width="14" height="11" viewBox="0 0 26 20"><rect x="1" y="1" width="24" height="18" fill="none" stroke="#fff" stroke-width="2.4"/><path d="M1 1l12 10L25 1" fill="none" stroke="#fff" stroke-width="2.4"/></svg><span>contact@corvend-media.example</span></div>
    </div>
    <div class="abs foot-col" style="left:948px;width:172px">
      <h5>Membership</h5>
      <div style="display:flex;gap:12px">
        <div class="badge" style="background:#fff"></div>
        <div class="badge" style="background:#111"></div>
      </div>
    </div>
  </footer>

  <div class="abs copyright" style="left:0;width:1164px">
    <span>COPYRIGHT © 2016 CORVEND MEDIA. ALL RIGHTS RESERVED.</span>
    <span class="social-dots"><i></i><i></i><i></i></span>
  </div>

</div>
</body>
</html>
```